New Design for Willow Glow & Laser

The name of our company is Willow Glow & Laser, and this is our current website: www.WillowGlowLaser.example. We are looking for a fresh design mock-up of our website.
What is important to us?
> We want to maintain the same navigation.
> We want to use the same content (e.g., text, pictures, etc.)
> We want to maintain the color scheme.
> The website aims to get visitors to BOOK ONLINE or BUY ONLINE.
Essential instructions for designers:
> Please visit our current website and our social media accounts to get a better idea of our brand design.
> We want a mockup design for our home page, service page, pricing page, before & after page, shop deals page, careers page, contact pages, and blog pages.
> Color codes: #faa641, #222222, #fffffe, #ea8103
Target Market(s)
women 25 - 45
Number of Pages Required
5+ page
Look and feel

```html
<!DOCTYPE html>
<html lang="en">
<head>
<meta charset="utf-8">
<title>Willow Glow &amp; Laser — Home</title>
<link href="https://fonts.googleapis.com/css2?family=Archivo+Black&family=DM+Sans:wght@400;500;700&family=Great+Vibes&family=Oswald:wght@500&display=swap" rel="stylesheet">
<style>
:root{
  --orange:#faa641;
  --orange-deep:#ea8103;
  --ink:#222222;
  --white:#fffffe;
  --cream:#f8f1e6;
  --sand:#e6d6c3;
  --muted:#8a8a8a;
  --line:#e2e2e2;
}
*{box-sizing:border-box;margin:0;padding:0}
html,body{width:1200px;height:4584px;overflow:hidden}
body{position:relative;background:var(--white);color:var(--ink);font-family:"DM Sans",sans-serif}
.abs{position:absolute}
.photo{position:absolute}
.display{font-family:"Archivo Black",sans-serif;letter-spacing:1.5px;text-transform:uppercase}
.script{font-family:"Great Vibes",cursive;color:var(--orange);font-size:34px;line-height:1}
.section-head{position:absolute;left:0;width:1200px;text-align:center}
.section-head .display{font-size:28px;margin-top:4px}

/* top bar */
.topbar{top:0;left:0;width:1200px;height:45px;background:#111}
.topbar .info{position:absolute;top:14px;font-size:12px;color:#bbb;display:flex;align-items:center;gap:10px}
.topbar .book{position:absolute;right:0;top:0;width:329px;height:45px;background:var(--orange);color:var(--white);font-size:13px;font-weight:700;display:flex;align-items:center;padding-left:50px;gap:10px;letter-spacing:.5px}

/* nav */
.nav{top:45px;left:0;width:1200px;height:89px;background:var(--white)}
.nav a{position:absolute;top:37px;font-size:13px;font-weight:700;color:var(--ink);text-decoration:none;letter-spacing:.5px;transform:translateX(-50%)}
.nav a.active{color:var(--orange)}
.nav .sep{position:absolute;top:33px;width:1px;height:22px;background:var(--line)}
.brand{display:flex;align-items:center;gap:8px;font-family:"DM Sans",sans-serif;font-weight:700}
.brand .dot{width:22px;height:22px;border-radius:50%;background:var(--orange)}
.nav .brand{position:absolute;left:600px;top:30px;transform:translateX(-50%);font-size:20px;color:var(--ink)}

/* hero */
.hero{top:134px;left:0;width:1200px;height:617px;background:var(--sand)}
.hero .photo{left:676px;top:0;width:524px;height:617px;background:linear-gradient(135deg,#3a2c24,#cbb39b 45%,#e9e2da)}
.hero h1{position:absolute;left:144px;top:140px;font-size:62px;line-height:80px;letter-spacing:3px}
.hero h1 .o{color:var(--orange)}
.hero .lead{position:absolute;left:144px;top:306px;font-size:16px;line-height:32px}
.btn{position:absolute;height:43px;display:flex;align-items:center;justify-content:center;font-size:13px;font-weight:700;color:var(--white);letter-spacing:.5px}
.btn.orange{background:var(--orange)}
.btn.dark{background:var(--ink)}
.hero .dots{position:absolute;left:146px;top:478px;display:flex;gap:14px}
.hero .dots i{width:9px;height:9px;transform:rotate(45deg);background:#999}
.hero .dots i.on{background:var(--orange)}
.hero .explore{position:absolute;left:55px;top:205px;writing-mode:vertical-rl;font-size:11px;letter-spacing:7px;color:#666}

/* about */
.about{top:751px;left:0;width:1200px;height:634px}
.frame{position:absolute;background:var(--white);padding:6px;box-shadow:0 2px 10px rgba(0,0,0,.12)}
.frame .photo{position:static;width:100%;height:100%}
.about .text{position:absolute;left:680px;top:132px;width:376px}
.about .text h2{font-size:30px;margin:6px 0 16px}
.about .text p{font-size:12.5px;line-height:19px;margin-bottom:19px;color:#333}

/* services */
.services{top:1385px;left:0;width:1200px;height:862px;background:var(--cream)}
.card{position:absolute;overflow:hidden;box-shadow:0 2px 6px rgba(0,0,0,.25)}
.card .photo{position:absolute;inset:0}
.card .label{position:absolute;left:8px;right:8px;bottom:8px;height:32px;background:var(--white);border-radius:6px;display:flex;align-items:center;justify-content:center;font-size:16px;font-weight:500}

/* deals */
.deals{top:2247px;left:0;width:1200px;height:602px}
.deal{position:absolute;top:201px;width:291px;height:328px;background:var(--white);border:1px solid var(--line);border-radius:6px}
.deal .photo{left:0;top:0;width:100%;height:272px;border-radius:6px 6px 0 0}
.deal .name{position:absolute;left:0;right:0;bottom:16px;text-align:center;font-size:17px;font-weight:500}
.deal .price{position:absolute;left:50%;top:-8px;transform:translateX(-50%);width:118px;height:54px;background:var(--orange);border-radius:0 0 59px 59px;color:var(--white);font-size:30px;font-weight:500;display:flex;align-items:center;justify-content:center}
.deal .price sup{font-size:15px;margin-right:2px}
.deal .blurb{position:absolute;left:40px;right:40px;top:85px;text-align:center;color:var(--white);font-size:14px;line-height:24px}
.deal .shop{display:block;color:var(--orange);font-size:12px;font-weight:700;margin-top:10px}
.deal .tag{position:absolute;left:20px;bottom:70px;background:var(--white);border-radius:10px;font-size:10px;padding:3px 10px;font-weight:500}
.circle-btn{position:absolute;width:36px;height:36px;border-radius:50%;background:#fdf0e0;display:flex;align-items:center;justify-content:center}

/* testimonials */
.testimonials{top:2849px;left:0;width:1200px;height:575px;background:var(--cream)}
.testimonials .photo{left:623px;top:83px;width:577px;height:410px;background:linear-gradient(120deg,#e7e4e2,#b9b2ad 50%,#3a3634)}
.testimonials h2{position:absolute;left:148px;top:138px;font-size:28px;line-height:36px}
.testimonials .quote{position:absolute;left:146px;top:236px;width:390px;font-size:15px;line-height:27px}
.avatar{position:absolute;left:145px;top:374px;width:56px;height:56px;border-radius:50%;background:#000}

/* gallery */
.gallery{top:3424px;left:0;width:1200px;height:520px}
.ba{position:absolute;top:176px;width:292px;height:312px}
.ba .photo{position:absolute;left:0;width:100%;height:155px;background:linear-gradient(180deg,#d69a94,#b86e70)}
.ba .before{top:0}
.ba .after{top:157px}
.ba .tag{position:absolute;background:var(--orange);color:var(--white);font-size:9px;font-weight:700;padding:3px 8px;letter-spacing:.5px}

/* follow */
.follow{top:3944px;left:0;width:1200px;height:338px}
.tile{position:absolute;top:147px;width:198px;height:190px}

/* footer */
.footer{top:4282px;left:0;width:1200px;height:302px;background:var(--ink);color:var(--white)}
.footer .vline{position:absolute;top:0;width:1px;height:302px;background:#3a3a3a}
.footer .mark{position:absolute;top:80px;width:3px;height:20px;background:var(--orange)}
.footer h4{position:absolute;top:78px;font-family:"Oswald",sans-serif;font-weight:500;font-size:19px}
.footer .small{position:absolute;font-size:11.5px;color:#777}
.footer .field{position:absolute;left:463px;top:148px;width:274px;height:43px;background:#2d2d2d;border-radius:3px;font-size:11.5px;color:#666;padding:13px 20px}
</style>
</head>
<body>

<!-- Top bar -->
<div class="abs topbar">
  <div class="info" style="left:148px">
    <svg width="16" height="13" viewBox="0 0 16 13" fill="none" stroke="#bbb" stroke-width="1.3"><rect x="1" y="1" width="14" height="11" rx="1"/><path d="M1 2l7 5 7-5"/></svg>
    hello@willowglowlaser.example
  </div>
  <div class="abs" style="left:380px;top:12px;width:1px;height:22px;background:#444"></div>
  <div class="info" style="left:400px">
    <svg width="14" height="16" viewBox="0 0 14 16" fill="none" stroke="#bbb" stroke-width="1.3"><path d="M7 15s-5-5-5-9a5 5 0 0110 0c0 4-5 9-5 9z"/><circle cx="7" cy="6" r="2"/></svg>
    Our Locations
  </div>
  <div class="book">
    <span style="width:14px;height:14px;border-radius:50%;background:var(--white);display:inline-block"></span>
    BOOK ONLINE
    <svg width="22" height="10" viewBox="0 0 22 10" fill="none" stroke="#fffffe" stroke-width="1.4"><path d="M0 5h20M16 1l4 4-4 4"/></svg>
  </div>
</div>

<!-- Navigation -->
<nav class="abs nav">
  <a class="active" style="left:167px">HOME</a>
  <span class="sep" style="left:226px"></span>
  <a style="left:294px">SERVICES</a>
  <span class="sep" style="left:370px"></span>
  <a style="left:433px">PRICING</a>
  <div class="brand"><span class="dot"></span>Willow Glow &amp; Laser</div>
  <a style="left:755px">ABOUT</a>
  <span class="sep" style="left:810px"></span>
  <a style="left:867px">BLOG</a>
  <span class="sep" style="left:945px"></span>
  <a style="left:1018px">CONTACT</a>
</nav>

<!-- Hero -->
<section class="abs hero">
  <div class="photo" role="img" aria-label="Aesthetician in a face mask treating a client reclining in a treatment chair"></div>
  <div class="explore">EXPLORE MORE</div>
  <h1 class="display">Your skin<br><span class="o">Deserves it</span></h1>
  <p class="lead">LASER CENTER &amp; MEDISPA located in<br>Downtown Phoenix, Tempe, Tucson, &amp; Yuma.</p>
  <div class="btn orange" style="left:144px;top:400px;width:159px">BOOK ONLINE</div>
  <div class="btn dark" style="left:328px;top:400px;width:156px">SHOP DEALS</div>
  <div class="dots"><i></i><i class="on"></i><i></i></div>
</section>

<!-- About -->
<section class="abs about">
  <div class="frame" style="left:147px;top:108px;width:283px;height:331px">
    <div class="photo" role="img" aria-label="Smiling technician holding a laser handpiece in a clinic" style="background:linear-gradient(160deg,#8b5a3c,#d8d0c8 55%,#2a2a2a)"></div>
  </div>
  <div class="frame" style="left:350px;top:252px;width:283px;height:300px">
    <div class="photo" role="img" aria-label="Gloved hands treating a client's face beside a green plant" style="background:linear-gradient(140deg,#e9e6e1,#7a8a5a 45%,#2b2b2b)"></div>
  </div>
  <div class="text">
    <div class="script">About us</div>
    <h2 class="display">Willow Glow &amp; Laser</h2>
    <p>At Willow Glow &amp; Laser, we've always believed that caring about your skin and your appearance is not selfish, it is self-care. It's time to be proud of the steps you take to look your best and it's time you ask for the best. Your skin deserves it.</p>
    <p>Willow Glow brings to you the latest technology, techniques, and the best professionals to deliver the results you want guaranteed.</p>
    <p>It's time to cross out the judgment, the labels, the hesitation, and the regrets.</p>
    <p>We offer clinic locations in Tucson, AZ, Phoenix, AZ, Tempe, AZ and Yuma, AZ.</p>
  </div>
</section>

<!-- Services -->
<section class="abs services">
  <div class="section-head" style="top:58px"><div class="script">Our Services</div><div class="display">What we offer</div></div>
  <div class="card" style="left:144px;top:180px;width:290px;height:283px"><div class="photo" role="img" aria-label="Client wearing purple eye shields during a photofacial" style="background:linear-gradient(150deg,#dcdcdc,#e8c4b0 55%,#2a2a2a)"></div><div class="label">Photofacials</div></div>
  <div class="card" style="left:454px;top:180px;width:290px;height:283px"><div class="photo" role="img" aria-label="Injector treating a red-haired client" style="background:linear-gradient(150deg,#e4e1dc,#6a4a3a 50%,#222)"></div><div class="label">Tox Injections</div></div>
  <div class="card" style="left:764px;top:180px;width:292px;height:283px"><div class="photo" role="img" aria-label="Client in protective glasses receiving laser hair removal on the jaw" style="background:linear-gradient(150deg,#efeeec,#d8b49e 55%,#1e1e1e)"></div><div class="label">Laser Hair Removal</div></div>
  <div class="card" style="left:144px;top:493px;width:444px;height:285px"><div class="photo" role="img" aria-label="Facial treatment with a wand device on a client's face" style="background:linear-gradient(160deg,#3a3a3a,#e0c2ad 50%,#bdbdbd)"></div><div class="label">Facials &amp; Peels</div></div>
  <div class="card" style="left:611px;top:493px;width:445px;height:285px"><div class="photo" role="img" aria-label="Gloved injector enhancing a client's lips" style="background:linear-gradient(160deg,#f1ece8,#d9a89a 50%,#1e1e1e)"></div><div class="label">Lip Shape &amp; Enhancement</div></div>
</section>

<!-- Deals -->
<section class="abs deals">
  <div class="section-head" style="top:46px"><div class="script">Deals</div><div class="display">Our shop deals</div></div>
  <div class="deal" style="left:144px">
    <div class="photo" role="img" aria-label="Two smiling women, one holding a hand mirror" style="background:linear-gradient(150deg,#e8e8e6,#caa28a 50%,#3a2a22)"></div>
    <div class="price"><sup>$</sup>80</div>
    <div class="name">Lip Shape Enhancement</div>
  </div>
  <div class="deal" style="left:455px">
    <div class="photo" role="img" aria-label="Dark background behind the deal description" style="background:#1f1f1f"></div>
    <div class="price"><sup>$</sup>159</div>
    <div class="blurb">Tox Cosmetic: The non-surgical wrinkle fighter! Relax muscles, smooth fine lines &amp; wrinkles, unleash your beauty confidence!<span class="shop">SHOP NOW &nbsp;➜</span></div>
    <div class="name">20 Units of Tox</div>
  </div>
  <div class="deal" style="left:765px">
    <div class="photo" role="img" aria-label="Client receiving a hydrogen facial with a glowing wand" style="background:linear-gradient(150deg,#f2f2f2,#d7b9a6 50%,#2a2a2a)"></div>
    <div class="price"><sup>$</sup>99</div>
    <div class="tag">One full face treatment</div>
    <div class="name">1 Hydrogen Facial</div>
  </div>
  <div class="circle-btn" style="left:1081px;top:333px"><svg width="8" height="12" viewBox="0 0 8 12" fill="none" stroke="#faa641" stroke-width="1.5"><path d="M1 1l5 5-5 5"/></svg></div>
</section>

<!-- Testimonials -->
<section class="abs testimonials">
  <div class="photo" role="img" aria-label="Technician treating a blonde client's face in a bright clinic"></div>
  <div class="script abs" style="left:142px;top:86px">Testimonials</div>
  <h2 class="display">What our happy<br>clients say</h2>
  <svg class="abs" style="left:490px;top:135px" width="74" height="50" viewBox="0 0 74 50" fill="#ddd"><path d="M30 0C12 4 0 16 0 32a16 16 0 1032 0c0-8-6-15-14-16 2-6 7-10 14-12z"/><path d="M72 0C54 4 42 16 42 32a16 16 0 1032 0c0-8-6-15-14-16 2-6 7-10 14-12z"/></svg>
  <p class="quote">"Awesome experience! Clean, professional, fast and painless laser hair removal services. Maya was a great technician and the whole experience was stress-free!"</p>
  <div class="avatar"></div>
  <div class="abs" style="left:223px;top:382px;font-size:15px;font-weight:500">Clara Benning</div>
  <div class="abs" style="left:223px;top:404px;font-size:12px;color:var(--muted)">Project Manager</div>
  <div class="circle-btn" style="left:452px;top:384px;background:#efe7dc"><svg width="8" height="12" viewBox="0 0 8 12" fill="none" stroke="#999" stroke-width="1.5"><path d="M7 1L2 6l5 5"/></svg></div>
  <div class="circle-btn" style="left:514px;top:384px"><svg width="8" height="12" viewBox="0 0 8 12" fill="none" stroke="#faa641" stroke-width="1.5"><path d="M1 1l5 5-5 5"/></svg></div>
</section>

<!-- Before & After -->
<section class="abs gallery">
  <div class="section-head" style="top:40px"><div class="script">Our works</div><div class="display">Before &amp; after gallery</div></div>
  <div class="ba" style="left:144px">
    <div class="photo before" role="img" aria-label="Lips before treatment"></div>
    <div class="photo after" role="img" aria-label="Lips after treatment"></div>
    <span class="tag" style="left:0;top:0">BEFORE</span><span class="tag" style="left:0;bottom:0">AFTER</span>
  </div>
  <div class="ba" style="left:454px">
    <div class="photo before" role="img" aria-label="Forehead lines before treatment" style="background:linear-gradient(180deg,#d9b8a0,#c79c82)"></div>
    <div class="photo after" role="img" aria-label="Smoothed forehead after treatment" style="background:linear-gradient(180deg,#d9b8a0,#b78a6e)"></div>
    <span class="tag" style="left:0;top:0">BEFORE</span><span class="tag" style="left:0;bottom:0">AFTER</span>
    <div class="abs" style="left:129px;top:138px;width:34px;height:34px;border-radius:50%;background:var(--white);display:flex;align-items:center;justify-content:center"><svg width="12" height="16" viewBox="0 0 12 16" fill="#888"><path d="M6 0l5 6H1zM6 16l-5-6h10z"/></svg></div>
  </div>
  <div class="ba" style="left:762px">
    <div class="photo before" role="img" aria-label="Lips before enhancement" style="background:linear-gradient(180deg,#d8a9a6,#c28c8c)"></div>
    <div class="photo after" role="img" aria-label="Fuller lips after enhancement" style="background:linear-gradient(180deg,#d49a98,#b06e74)"></div>
    <span class="tag" style="left:0;top:0">BEFORE</span><span class="tag" style="left:0;bottom:0">AFTER</span>
  </div>
</section>

<!-- Follow us -->
<section class="abs follow">
  <div class="section-head" style="top:40px"><div class="script">Social media</div><div class="display">Follow us</div></div>
  <div class="tile" style="left:0;background:linear-gradient(160deg,#e9e9e9,#9a8a7a)" role="img" aria-label="Team members smiling together"></div>
  <div class="tile" style="left:200px;background:linear-gradient(160deg,#ddd,#4a3a32)" role="img" aria-label="Clients posing with a hand mirror"></div>
  <div class="tile" style="left:400px;background:linear-gradient(160deg,#f0e6dc,#b08a70)" role="img" aria-label="Client holding a mirror after treatment"></div>
  <div class="tile" style="left:600px;background:var(--orange);opacity:.9" role="img" aria-label="Highlighted social post of a smiling client"></div>
  <div class="tile" style="left:800px;background:linear-gradient(160deg,#f2f2f2,#6a4a3a)" role="img" aria-label="Client with curly hair smiling"></div>
  <div class="tile" style="left:1000px;background:linear-gradient(160deg,#eee,#2a2420)" role="img" aria-label="Client receiving a facial treatment"></div>
</section>

<!-- Footer -->
<footer class="abs footer">
  <div class="vline" style="left:393px"></div>
  <div class="vline" style="left:790px"></div>
  <div class="mark" style="left:392px"></div>
  <div class="mark" style="left:789px"></div>
  <div class="brand abs" style="left:214px;top:128px;transform:translateX(-50%);font-size:19px;color:var(--white);white-space:nowrap"><span class="dot"></span>Willow Glow &amp; Laser</div>
  <h4 style="left:463px">Newsletter</h4>
  <div class="small" style="left:463px;top:114px">Subscribe our newsletter for latest news</div>
  <div class="field">Enter your email</div>
  <svg class="abs" style="left:706px;top:162px" width="16" height="14" viewBox="0 0 16 14" fill="none" stroke="#faa641" stroke-width="1.3"><path d="M1 1l14 6-14 6 3-6z"/></svg>
  <div class="small" style="left:470px;top:240px;font-size:10.5px;color:#666">© 2024 Willow Glow &amp; Laser. All Rights Reserved.</div>
  <h4 style="left:840px">Our Locations</h4>
  <div class="small" style="left:840px;top:150px;line-height:24px">Downtown Phoenix, AZ<br>Tucson, AZ<br>Yuma, AZ<br>Tempe, AZ</div>
</footer>

</body>
</html>
```